Virtual Assistant/Online Marketing Business Card/Stationary

I need a professional but modern business card/stationary for my company in Dallas called Brivolo. Brivolo is a virtual assistant specializing in online marketing. I would like a unique design that stands out and makes my brand clear. Incorporating the logo is a must and have attached it to this brief.

Target Market(s)

small business owners & entrepreneurs, 35-65

Industry/Entity Type

Business

Contact Information for Business Card

Maren Tolk
marentolk@brivolo.biz
(555) 271-9064
brivolo.biz

Font styles to use
Sans Serif

Colors
f04a50
3176b5
9bcb3c

Requirements
Must have
• Colors that match the logo colors. Logo integration

```html
<!DOCTYPE html>
<html lang="en">
<head>
<meta charset="utf-8">
<title>Brivolo — Business Card</title>
<link rel="stylesheet" href="https://fonts.googleapis.com/css2?family=Ubuntu:wght@300;400;500;700&display=swap">
<style>
  :root {
    --brand-red: #f04a50;
    --brand-blue: #3176b5;
    --brand-green: #9bcb3c;
    --ink: #2b2b2b;
    --ink-soft: #8a8a8a;
    --card: #ffffff;
    --canvas: #ececec;
    --pattern-blue: rgba(49, 118, 181, 0.16);
    --pattern-green: rgba(155, 203, 60, 0.14);
  }
  * { box-sizing: border-box; margin: 0; padding: 0; }
  html, body {
    width: 1200px;
    height: 900px;
    overflow: hidden;
    background: var(--canvas);
    font-family: "Ubuntu", sans-serif;
  }
  .stage {
    position: relative;
    width: 1200px;
    height: 900px;
  }
  .card {
    position: absolute;
    width: 525px;
    height: 300px;
    background: var(--card);
    overflow: hidden;
    box-shadow: 0 6px 18px rgba(0, 0, 0, 0.18);
  }
  .card--front { left: 70px; top: 200px; }
  .card--back { left: 605px; top: 400px; }

  .pattern {
    position: absolute;
  }
  .pattern--front-top {
    right: 0; top: 0; width: 240px; height: 170px;
    background: radial-gradient(ellipse at top right, var(--pattern-blue), var(--pattern-green) 45%, transparent 75%);
  }
  .pattern--front-bottom {
    left: 0; bottom: 0; width: 340px; height: 120px;
    background: radial-gradient(ellipse at bottom left, rgba(49,118,181,0.22), var(--pattern-blue) 40%, transparent 75%);
  }
  .pattern--back-right {
    right: 0; top: 0; width: 230px; height: 300px;
    background: radial-gradient(ellipse at right center, var(--pattern-green), var(--pattern-blue) 45%, transparent 78%);
  }
  .pattern--back-bottom {
    left: 0; bottom: 0; width: 300px; height: 100px;
    background: radial-gradient(ellipse at bottom left, rgba(49,118,181,0.22), var(--pattern-blue) 40%, transparent 75%);
  }

  .brand {
    position: absolute;
    left: 0; right: 0; top: 95px;
    text-align: center;
  }
  .brand__name {
    display: inline-flex;
    align-items: center;
    gap: 10px;
    font-size: 46px;
    font-weight: 700;
    color: var(--ink);
    letter-spacing: -0.5px;
  }
  .brand__mark {
    width: 16px; height: 16px;
    background: var(--brand-red);
  }
  .brand__tagline {
    margin-top: 10px;
    font-size: 12px;
    font-weight: 300;
    color: var(--ink-soft);
  }

  .contact {
    position: absolute;
    left: 28px; top: 72px;
  }
  .contact__name {
    font-size: 20px;
    font-weight: 500;
    color: var(--ink);
    margin-bottom: 16px;
  }
  .contact__list { list-style: none; }
  .contact__item {
    display: flex;
    align-items: center;
    gap: 12px;
    font-size: 12px;
    font-weight: 300;
    color: var(--ink-soft);
    height: 26px;
  }
  .contact__icon { width: 16px; height: 16px; flex: none; }
</style>
</head>
<body>
<main class="stage">

  <section class="card card--front" aria-label="Card front">
    <div class="pattern pattern--front-top" role="img" aria-label="Soft pattern of translucent blue and green diamond squares"></div>
    <div class="pattern pattern--front-bottom" role="img" aria-label="Soft pattern of outlined blue diamond squares"></div>
    <div class="brand">
      <div class="brand__name"><span class="brand__mark"></span>Brivolo</div>
      <p class="brand__tagline">virtual assistant for online marketing</p>
    </div>
  </section>

  <section class="card card--back" aria-label="Card back">
    <div class="pattern pattern--back-right" role="img" aria-label="Soft pattern of translucent blue and green diamond squares"></div>
    <div class="pattern pattern--back-bottom" role="img" aria-label="Soft pattern of outlined blue diamond squares"></div>
    <div class="contact">
      <h1 class="contact__name">Maren Tolk</h1>
      <ul class="contact__list">
        <li class="contact__item">
          <svg class="contact__icon" viewBox="0 0 16 16" aria-hidden="true">
            <path fill="var(--brand-green)" d="M3.6 1.5l2.2 2.6-1.3 1.6c.9 2 2.6 3.8 4.7 4.8l1.6-1.3 2.6 2.2-1.3 2.2C6.9 15 1 9.1 1.5 3.6z"/>
          </svg>
          <span>(555) 271-9064</span>
        </li>
        <li class="contact__item">
          <svg class="contact__icon" viewBox="0 0 16 16" aria-hidden="true">
            <rect x="1" y="3" width="14" height="10" rx="1" fill="var(--brand-red)"/>
            <path d="M1.5 4l6.5 5 6.5-5" fill="none" stroke="#fff" stroke-width="1.2"/>
          </svg>
          <span>marentolk@brivolo.biz</span>
        </li>
        <li class="contact__item">
          <svg class="contact__icon" viewBox="0 0 16 16" aria-hidden="true">
            <path fill="var(--brand-blue)" d="M8 1a5 5 0 0 0-5 5c0 3.6 5 9 5 9s5-5.4 5-9a5 5 0 0 0-5-5z"/>
            <circle cx="8" cy="6" r="1.8" fill="#fff"/>
          </svg>
          <span>brivolo.biz</span>
        </li>
      </ul>
    </div>
  </section>

</main>
</body>
</html>
```